Wedding Brochure/Booklet for Fern & The Heron

We have the content and a previous attempt already. We just need some edits and then have a version we can email as a PDF and Print as a Booklet.

Any further improvements to the visual aspect would also be welcomed

Check out our website to see who we are www.fernandtheheron-example.com

Target Market(s)

Couples!!!!

Industry/Entity Type

Wedding

Font styles to use
Sans Serif
Decorative
Script

Requirements
Must have
• Style
Nice to have
• Style & Elegance
Should not have
• Too bold or Bright Colours

```html
<!DOCTYPE html>
<html lang="en">
<head>
<meta charset="utf-8">
<title>Fern &amp; The Heron — Wedding Brochure Spread</title>
<link href="https://fonts.googleapis.com/css2?family=Parisienne&family=Tenor+Sans&display=swap" rel="stylesheet">
<style>
  :root {
    --backdrop: #e9e9ea;
    --paper: #f6f6f7;
    --paper-edge: #e2e2e5;
    --ink: #5a5870;
    --ink-soft: #6f6d80;
    --ornament: #d3d2e3;
    --scene-light: #d9d9dc;
    --scene-dark: #6c6c70;
  }
  * { box-sizing: border-box; margin: 0; padding: 0; }
  html, body {
    width: 1200px; height: 1200px; overflow: hidden;
    background: var(--backdrop);
  }
  .spread {
    position: absolute;
    left: 110px; top: 185px;
    width: 980px; height: 700px;
    display: flex;
    box-shadow: 0 14px 40px rgba(60, 60, 70, 0.14);
  }
  .page {
    position: relative;
    width: 490px; height: 700px;
    background: var(--paper);
    overflow: hidden;
    font-family: "Tenor Sans", "Gill Sans", sans-serif;
    color: var(--ink);
    text-align: center;
  }
  .page--left { border-right: 1px solid var(--paper-edge); }
  .ornament {
    position: absolute;
    background: linear-gradient(90deg, transparent, var(--ornament) 20%, var(--ornament) 80%, transparent);
    opacity: 0.55;
  }
  .ornament--top { left: 40px; right: 40px; top: 18px; height: 70px; border-radius: 40px; }
  .ornament--bottom { left: 40px; right: 40px; bottom: 30px; height: 70px; border-radius: 40px; }
  .script-title {
    font-family: "Parisienne", cursive;
    font-weight: 400;
    color: var(--ink);
    font-size: 30px;
  }
  .page--left .script-title { margin-top: 120px; }
  .intro {
    width: 360px; margin: 14px auto 0;
    font-size: 11.5px; line-height: 1.45;
    color: var(--ink-soft);
  }
  .scene {
    position: absolute;
    left: 0; right: 0; bottom: 0; height: 380px;
    background: linear-gradient(180deg, var(--paper) 0%, var(--scene-light) 18%, #a8a8ac 55%, var(--scene-dark) 100%);
  }
  .page--right .script-title { margin-top: 110px; }
  .package { margin-top: 34px; }
  .package__name {
    font-variant: small-caps;
    font-weight: 400;
    font-size: 17px; letter-spacing: 0.04em;
    margin-bottom: 20px;
  }
  .package__items {
    list-style: none;
    font-size: 14.5px; line-height: 1.3;
  }
  .package + .package { margin-top: 48px; }
</style>
</head>
<body>
  <main class="spread">
    <section class="page page--left">
      <div class="ornament ornament--top" role="img" aria-label="Faint lavender vine-and-heart ornament"></div>
      <h1 class="script-title">Congratulations on your wedding!</h1>
      <p class="intro">Fern &amp; The Heron is the perfect venue for Weddings or Engagement Parties. The all in one venue has perfectly manicured gardens ideal for a wedding ceremony or a beautiful outdoor garden wedding. We have multiple rooms and spaces for you to choose from and packages for smaller Cocktail Weddings up to a sit down for 200 people.</p>
      <div class="scene" role="img" aria-label="Pencil-sketch style illustration of a couple in a garden overlooking the water, with vine ornaments"></div>
    </section>
    <section class="page page--right">
      <div class="ornament ornament--top" role="img" aria-label="Faint lavender vine-and-heart ornament"></div>
      <h2 class="script-title">Wedding Packages</h2>
      <div class="package">
        <h3 class="package__name">The Ashby</h3>
        <ul class="package__items">
          <li>Champagne at Ceremony</li>
          <li>8 Canapes – Heron Canape Menu</li>
          <li>Wedding Cake Served as dessert</li>
          <li>3.5 hr Beverage Package</li>
          <li>120 p/p</li>
        </ul>
      </div>
      <div class="package">
        <h3 class="package__name">The Riverbend</h3>
        <ul class="package__items">
          <li>Champagne at Ceremony</li>
          <li>Oysters on Arrival</li>
          <li>8 Canapes</li>
          <li>Supper Bowl</li>
          <li>Wedding Cake Served as dessert</li>
          <li>4.5hr Beverage Package</li>
          <li>155 p/p</li>
        </ul>
      </div>
      <div class="ornament ornament--bottom" role="img" aria-label="Faint lavender vine-and-heart ornament"></div>
    </section>
  </main>
</body>
</html>
```